VLK IT Solutions Provider

Please read attached documentation completely before beginning Project. Thank you!

Folio Nest Project Requirements

Thank you for your interest in this design contest. We are always welcome to questions and are looking forward to seeing what you can come up with.

The logo is located on the current site homepage http://www.vantolirex.com/

Bootstrap

We work on a Bootstrap platform with our custom built CMS. We require all designs to be

sized accordingly with the bootstrap grid system found here: http://trelvanix.com/css/#grid

Start of Competition Requirements

At the start of a competition, we are looking for general Home Page Design concepts and interior page design concepts as well.

HOME PAGE DESIGN

Any changes requested by the client in the original designs

Responsive Tablet View (using standard bootstrap media queries, we need to see an

example of a tablet size home page view)

Responsive Phone View (using standard bootstrap media queries, we need to see an

example of a phone size home page view)

INTERIOR PAGE DESIGN

These pages are general content pages. Our CMS allows for the creation of unlimited

pages and gives the client control of adding them. Interior Page Designs can be built

with 1 column, 2 columns (either right side bar or left sidebar)

Examples of buttons and button states,

Examples of drop down menus

Examples of H1 through H5 plus body copy

We uploaded a clean logo to use on the project. Thank you.

Project Deadline Extended

We added a updated Creative Brief document to help out. Please take a look thanks!

```html
<!DOCTYPE html>
<html lang="en">
<head>
<meta charset="utf-8">
<title>VLK — Technology Solutions for National Defense &amp; Global Security</title>
<link rel="stylesheet" href="https://fonts.googleapis.com/css2?family=Roboto+Condensed:wght@300;400;700&family=Arimo:wght@400;700&display=swap">
<style>
:root{
  --brand:#0b4f9c;
  --brand-soft:#5b86b3;
  --ink:#1d1d1d;
  --muted:#555;
  --header-bg:#f7f7f7;
  --line:#e6e6e6;
  --social-band:#2d313b;
  --social-tile:#383c46;
  --footer-bg:#c9c9c9;
  --bottom-bar:#121212;
  --white:#fff;
  --accent-blue:#4a90d9;
}
*{box-sizing:border-box;margin:0;padding:0}
html,body{width:764px;height:1200px;overflow:hidden}
body{position:relative;background:var(--white);font-family:"Arimo",Arial,sans-serif;color:var(--ink)}
a{text-decoration:none}
.abs{position:absolute}

/* Header */
.site-header{left:0;top:0;width:764px;height:60px;background:var(--header-bg);box-shadow:0 1px 3px rgba(0,0,0,.15);z-index:2}
.brand{left:64px;top:8px;color:var(--brand);font-family:"Roboto Condensed",sans-serif;font-weight:700;line-height:1}
.brand-name{font-size:34px;letter-spacing:-1px;display:block}
.brand-tag{font-size:6.5px;display:block;margin-top:2px;letter-spacing:.1px}
.top-contact{top:17px;font-size:7px;color:var(--muted);display:flex;align-items:center;gap:4px}
.top-social{left:628px;top:14px;display:flex;gap:1px}
.top-social span{width:16px;height:16px;background:var(--brand)}
.nav-link{top:42px;font-family:"Roboto Condensed",sans-serif;font-size:8px;font-weight:700;text-transform:uppercase;color:#222;white-space:nowrap}
.nav-link.is-active{color:var(--brand)}
.nav-underline{left:458px;top:55px;width:34px;height:2px;background:var(--brand)}
.nav-search{left:682px;top:38px}

/* Hero */
.hero{left:0;top:60px;width:764px;height:340px;background:linear-gradient(180deg,#cacaca,#bebebe);overflow:hidden}
.hero-art{position:absolute;left:0;top:0;width:764px;height:340px;background:
  radial-gradient(ellipse 235px 250px at 385px 300px,#8fa9c2 0,#7f9bb7 55%,#aebdcb 80%,rgba(196,198,200,0) 100%)}
.hero-title{position:absolute;left:0;top:200px;width:764px;text-align:center;color:var(--white);font-family:"Roboto Condensed",sans-serif;font-weight:400;font-size:21.5px;line-height:27px;text-transform:uppercase;text-shadow:0 1px 2px rgba(0,0,0,.25)}
.btn{display:flex;align-items:center;justify-content:center;font-family:"Roboto Condensed",sans-serif;font-weight:700;font-size:7.5px;text-transform:uppercase;color:var(--white)}
.btn-hero-primary{left:272px;top:274px;width:107px;height:19px;background:var(--brand-soft);border:1px solid #eee}
.btn-hero-ghost{left:385px;top:274px;width:108px;height:19px;border:1px solid #f0f0f0}

/* Welcome */
.section-title{left:0;width:764px;text-align:center;font-family:"Roboto Condensed",sans-serif;font-weight:300;font-size:17px;color:#111;text-transform:uppercase}
.welcome-copy{left:186px;top:474px;width:392px;text-align:center;font-size:6.8px;line-height:9.5px;color:#222}
.btn-outline{left:329px;top:518px;width:107px;height:19px;border:1px solid #666;color:#222;font-weight:400}
.divider{left:123px;top:572px;width:518px;height:1px;background:var(--line)}

/* Hiring tiles */
.career-tile{width:113px;height:88px;border:1px solid #ececec;background:var(--white);display:flex;flex-direction:column;align-items:center;color:#222;font-family:"Roboto Condensed",sans-serif;font-size:11px}
.career-tile svg{margin-top:17px;height:30px}
.career-tile span{margin-top:14px}
.career-tile.is-featured{background:#f2f2f2;color:var(--brand);font-weight:700}

/* Social band */
.social-band{left:0;top:970px;width:764px;height:53px;background:var(--social-band)}
.social-band span{position:absolute;top:11px;width:32px;height:32px;background:var(--social-tile)}
.social-band span.is-active{background:var(--accent-blue)}

/* Footer */
.site-footer{left:0;top:1023px;width:764px;height:142px;background:var(--footer-bg)}
.footer-heading{position:absolute;top:22px;font-family:"Roboto Condensed",sans-serif;font-weight:400;font-size:11.5px;color:#222}
.footer-text{position:absolute;font-size:6.2px;line-height:7.6px;color:#444}
.footer-links{position:absolute;left:250px;top:42px;list-style:none;font-size:6.2px;line-height:12.5px;color:#444}
.footer-links li::before{content:"› ";font-weight:700}
.footer-links li.is-active{color:var(--accent-blue)}
.blog-thumb{position:absolute;left:395px;width:31px;height:29px;background:linear-gradient(135deg,#e8e8e8,#6f6f6f)}
.footer-address strong{font-weight:700;color:#333}

.bottom-bar{left:0;top:1165px;width:764px;height:35px;background:var(--bottom-bar)}
.copyright{position:absolute;left:75px;top:14px;font-size:6.2px;color:#666}
.btn-footer{left:583px;top:8px;width:107px;height:19px;background:var(--brand)}
</style>
</head>
<body>

<header class="site-header abs">
  <a class="brand abs" href="#">
    <span class="brand-name">VLK</span>
    <span class="brand-tag">VANTOLIREX RESEARCH CORPORATION</span>
  </a>
  <div class="top-contact abs" style="left:479px">
    <svg width="9" height="7" viewBox="0 0 9 7"><rect x=".5" y=".5" width="8" height="6" fill="none" stroke="#0b4f9c"/><path d="M.5 .5l4 3.5 4-3.5" fill="none" stroke="#0b4f9c"/></svg>
    info@VLK.com
  </div>
  <div class="top-contact abs" style="left:551px">
    <svg width="8" height="8" viewBox="0 0 8 8"><path d="M1 1c0 4 2 6 6 6l.5-1.5-1.8-1-1 1C3.5 5 3 4.5 2.5 3.3l1-1-1-1.8z" fill="#0b4f9c"/></svg>
    P. (555) 014-2387
  </div>
  <div class="top-social abs" aria-label="Social links"><span></span><span></span><span></span><span></span></div>
  <nav>
    <a class="nav-link is-active abs" href="#" style="left:465px">Home</a>
    <a class="nav-link abs" href="#" style="left:500px">About VLK</a>
    <a class="nav-link abs" href="#" style="left:553px">Divisions</a>
    <a class="nav-link abs" href="#" style="left:603px">Products/Services</a>
  </nav>
  <div class="nav-underline abs"></div>
  <svg class="nav-search abs" width="15" height="15" viewBox="0 0 15 15"><circle cx="6" cy="6" r="4.6" fill="none" stroke="#111" stroke-width="1.8"/><path d="M9.5 9.5l4.5 4.5" stroke="#111" stroke-width="2"/></svg>
</header>

<section class="hero abs">
  <div class="hero-art" role="img" aria-label="Low-poly globe illustration with a network of connected points"></div>
  <h1 class="hero-title">Technology Solutions for National<br>Defense &amp; Global Security</h1>
  <a class="btn btn-hero-primary abs" href="#">Contact Us</a>
  <a class="btn btn-hero-ghost abs" href="#">Learn More</a>
</section>

<h2 class="section-title abs" style="top:440px">Welcome</h2>
<p class="welcome-copy abs">Since 1988, Vantolirex Research Corporation has been providing innovative and cost-effective products and services to customers worldwide. We are a vital source for leading-edge technology solutions that help our customers respond to opportunities faster, achieve more from their operations, and exceed their requirements.</p>
<a class="btn btn-outline abs" href="#">Learn More</a>
<div class="divider abs"></div>

<h2 class="section-title abs" style="top:601px">We're Hiring</h2>

<a class="career-tile abs" href="#" style="left:123px;top:643px">
  <svg width="32" viewBox="0 0 32 30"><circle cx="11" cy="9" r="5"/><circle cx="20" cy="9" r="5"/><path d="M2 24c0-6 4-9 9-9s9 3 9 9z"/><path d="M13 24c0-6 3-9 7-9 5 0 9 3 9 9z"/></svg>
  <span>A Career at VLK</span></a>
<a class="career-tile abs" href="#" style="left:259px;top:643px">
  <svg width="30" viewBox="0 0 30 30"><path d="M15 1l3 3 4-1 1 4 4 1-1 4 3 3-3 3 1 4-4 1-1 4-4-1-3 3-3-3-4 1-1-4-4-1 1-4-3-3 3-3-1-4 4-1 1-4 4 1z"/><circle cx="15" cy="15" r="8" fill="#fff"/><path d="M11 15l3 3 5-6" fill="none" stroke="#000" stroke-width="2"/></svg>
  <span>Benefits</span></a>
<a class="career-tile is-featured abs" href="#" style="left:394px;top:643px">
  <svg width="20" viewBox="0 0 20 40" style="height:38px;margin-top:12px"><path d="M6 1h8l-2 5H8z" fill="#0b4f9c"/><path d="M8 6h4l4 24-6 8-6-8z" fill="#fff" stroke="#0b4f9c" stroke-width="1.5"/><path d="M6 14l8-4M5 20l10-5M5 26l11-6M7 31l8-4" stroke="#0b4f9c" stroke-width="1.4"/></svg>
  <span style="margin-top:11px">Corporate Culture</span></a>
<a class="career-tile abs" href="#" style="left:529px;top:643px">
  <svg width="30" viewBox="0 0 30 30" fill="none" stroke="#000" stroke-width="3"><path d="M10 8l5-6 5 7"/><path d="M24 13l3 7-6 6"/><path d="M14 26H4l3-8"/></svg>
  <span>Our Hiring Process</span></a>

<a class="career-tile abs" href="#" style="left:123px;top:748px">
  <svg width="30" viewBox="0 0 30 30"><circle cx="15" cy="9" r="7"/><path d="M1 29c0-8 6-12 14-12s14 4 14 12z"/></svg>
  <span>Student Opportunities</span></a>
<a class="career-tile abs" href="#" style="left:259px;top:748px">
  <svg width="30" viewBox="0 0 30 30"><circle cx="11" cy="11" r="8" fill="none" stroke="#000" stroke-width="3"/><path d="M17 17l10 10" stroke="#000" stroke-width="4"/></svg>
  <span>Job Search</span></a>
<a class="career-tile abs" href="#" style="left:394px;top:748px">
  <svg width="32" viewBox="0 0 32 32"><circle cx="16" cy="16" r="14" fill="none" stroke="#000" stroke-width="2.5"/><circle cx="16" cy="9" r="2"/><rect x="14" y="13" width="4" height="11"/></svg>
  <span>How to Apply</span></a>
<a class="career-tile abs" href="#" style="left:529px;top:748px">
  <svg width="36" viewBox="0 0 36 30"><path d="M17 3h2v22h-2zM11 27h14v2H11zM5 7h26v2H5z"/><path d="M8 9l-5 10h10zM28 9l-5 10h10z" fill="none" stroke="#000" stroke-width="1.5"/><path d="M2 19h12a6 4 0 01-12 0zM22 19h12a6 4 0 01-12 0z"/></svg>
  <span>EEO is the Law</span></a>

<a class="career-tile abs" href="#" style="left:259px;top:854px">
  <svg width="32" viewBox="0 0 32 32"><circle cx="16" cy="17" r="13" fill="none" stroke="#000" stroke-width="1.8"/><path d="M16 17V4a13 13 0 0113 13z"/><path d="M16 17l-11 7M16 17l3 13" stroke="#000" stroke-width="1.5"/></svg>
  <span>Diversity</span></a>
<a class="career-tile abs" href="#" style="left:394px;top:854px">
  <svg width="34" viewBox="0 0 34 30"><rect x="2" y="3" width="24" height="22" fill="none" stroke="#000" stroke-width="2"/><rect x="2" y="3" width="24" height="5"/><path d="M6 12h3v3H6zm5 0h3v3h-3zm5 0h3v3h-3zM6 18h3v3H6zm5 0h3v3h-3z"/><circle cx="24" cy="20" r="5" fill="#fff" stroke="#000" stroke-width="2"/><path d="M28 24l5 5" stroke="#000" stroke-width="2.5"/></svg>
  <span>Recruiting Events</span></a>

<div class="social-band abs" aria-label="Social links">
  <span style="left:176px"></span><span style="left:223px"></span><span style="left:270px"></span>
  <span style="left:318px"></span><span class="is-active" style="left:365px"></span><span style="left:413px"></span>
  <span style="left:460px"></span><span style="left:507px"></span><span style="left:555px"></span>
</div>

<footer class="site-footer abs">
  <h3 class="footer-heading" style="left:76px">About Us</h3>
  <p class="footer-text" style="left:76px;top:43px;width:130px">Pellentesque habitant morbi tristique senectus et netus et malesuada fames ac turpis egestas. Vestibulum tortor quam, feugiat vitae, ultricies eget, tempor sit amet, ante.</p>
  <p class="footer-text" style="left:76px;top:91px;width:130px">Pellentesque habitant morbi tristique senectus.</p>

  <h3 class="footer-heading" style="left:250px">Company</h3>
  <ul class="footer-links">
    <li class="is-active">HOME</li><li>ABOUT VLK</li><li>DIVISIONS</li><li>PRODUCTS/SERVICES</li>
  </ul>

  <h3 class="footer-heading" style="left:394px">Latest Blog</h3>
  <div class="blog-thumb" style="top:41px" role="img" aria-label="Blog post photo of business people"></div>
  <p class="footer-text" style="left:431px;top:42px;width:92px">Pellentesque habitant morbi tristique senectus</p>
  <p class="footer-text" style="left:431px;top:65px">Posted 17 Aug 2013</p>
  <div class="blog-thumb" style="top:80px" role="img" aria-label="Blog post photo of a business meeting"></div>
  <p class="footer-text" style="left:431px;top:81px;width:92px">Pellentesque habitant morbi tristique senectus</p>
  <p class="footer-text" style="left:431px;top:104px">Posted 17 Aug 2013</p>

  <h3 class="footer-heading" style="left:564px">Address</h3>
  <p class="footer-text footer-address" style="left:564px;top:42px;width:120px"><strong>Vantolirex Research Corporation</strong></p>
  <p class="footer-text" style="left:564px;top:52px;width:120px">1480 Harlow Crest Avenue,<br>Suite 210 North<br>Marren, GA 30991</p>
  <p class="footer-text" style="left:564px;top:78px;width:120px">P. (555) 014-2387</p>
</footer>

<div class="bottom-bar abs">
  <p class="copyright">Copyright 2014 © Vantolirex Research Corporation. All rights reserved.</p>
  <a class="btn btn-footer abs" href="#">Contact Us</a>
</div>

</body>
</html>
```